Website banner

Here is the link where the current banner is featured https://www.brimlark.com.au/collections/gel-blasters

I need the banner recreated into desktop and mobile format size.
Update the key points to:
- FREE SHIPPING AUSTRALIA WIDE
- SAME DAY DISPATCH
- BEST PRICE GUARANTEE
- 3000+ 5 STAR REVIEWS
- BEST SERVICE & WARRANTY
- 100% SECURE CHECKOUT

I want the banner to suit the style of the website and make it look better than the last graphic.

I also need the "save even more" picture to be recreated as it looks very plain at the moment,

```html
<!DOCTYPE html>
<html lang="en">
<head>
<meta charset="UTF-8">
<title>Save Even More – Order Discounts</title>
<link rel="stylesheet" href="https://fonts.googleapis.com/css2?family=Bebas+Neue&display=swap">
<style>
  :root {
    --bg: #0a0a0a;
    --red: #e0232d;
    --splash: #7a0e13;
    --splash-dark: #5e0a0e;
    --white: #ffffff;
  }
  html, body {
    margin: 0;
    padding: 0;
    width: 1200px;
    height: 644px;
    overflow: hidden;
    background: var(--bg);
  }
  .banner {
    position: relative;
    width: 1200px;
    height: 644px;
    overflow: hidden;
    background: var(--bg);
    font-family: "Bebas Neue", "Oswald", sans-serif;
    color: var(--white);
  }
  .paint-splash {
    position: absolute;
    inset: 0;
    width: 1200px;
    height: 644px;
  }
  .headline {
    position: absolute;
    left: 181px;
    top: 97px;
    width: 627px;
    height: 99px;
    margin: 0;
    box-sizing: border-box;
    padding-left: 12px;
    background: var(--red);
    font-weight: 400;
    font-size: 118px;
    line-height: 112px;
    letter-spacing: 0.5px;
    white-space: nowrap;
  }
  .offer-list {
    margin: 0;
    padding: 0;
    list-style: none;
  }
  .offer {
    position: absolute;
    left: 181px;
    height: 70px;
  }
  .offer--250 { top: 270px; }
  .offer--500 { top: 360px; }
  .offer--1000 { top: 500px; }
  .offer-threshold {
    position: absolute;
    left: 0;
    top: 0;
    font-size: 96px;
    line-height: 80px;
    white-space: nowrap;
  }
  .offer-plus {
    font-size: 58px;
    vertical-align: 4px;
  }
  .offer-reward {
    position: absolute;
    top: 4px;
    height: 54px;
    box-sizing: border-box;
    padding-left: 10px;
    background: var(--red);
    font-size: 72px;
    line-height: 64px;
    white-space: nowrap;
    overflow: hidden;
  }
  .offer--250 .offer-reward { left: 404px; width: 366px; }
  .offer--500 .offer-reward { left: 431px; width: 346px; padding-left: 20px; }
  .offer--1000 .offer-reward { left: 422px; width: 416px; }
</style>
</head>
<body>
  <div class="banner">
    <svg class="paint-splash" viewBox="0 0 1200 644" role="img" aria-label="Dark red paint splatter sweeping diagonally across the background">
      <path fill="var(--splash)" d="M430 0 L1200 0 L1200 90 C1130 150 1080 230 1040 300 C1010 360 990 420 975 480 C960 540 930 600 880 644 L110 644 C150 590 220 520 280 450 C320 390 330 320 360 250 C380 180 400 90 430 0 Z"/>
      <path fill="var(--splash-dark)" d="M1000 0 L1200 0 L1200 90 C1150 130 1110 180 1080 230 C1060 160 1030 80 1000 0 Z"/>
      <circle cx="1060" cy="520" r="14" fill="var(--splash)"/>
      <circle cx="1110" cy="440" r="8" fill="var(--splash)"/>
      <circle cx="90" cy="610" r="12" fill="var(--splash)"/>
    </svg>

    <h1 class="headline">SAVE EVEN MORE!</h1>

    <ul class="offer-list">
      <li class="offer offer--250">
        <span class="offer-threshold">ORDER $250<span class="offer-plus">+</span></span>
        <span class="offer-reward">GET 5%OFF</span>
      </li>
      <li class="offer offer--500">
        <span class="offer-threshold">ORDER $500<span class="offer-plus">+</span></span>
        <span class="offer-reward">GET 10% OFF</span>
      </li>
      <li class="offer offer--1000">
        <span class="offer-threshold">ORDER $1000<span class="offer-plus">+</span></span>
        <span class="offer-reward">GET 15% OFF</span>
      </li>
    </ul>
  </div>
</body>
</html>
```